General Contractors need a new Crisp updated Card Design

We need a new business card design for our company of 25 years based in Dunmore Vale call Pollvarn Building Inc. : Our goal is to be the leading commercial contractors in Dunmore Vale by providing exceptional value to our clients. We work very hard to deliver professional, quality, service in conjunction with consistent price competitiveness to all of our clients on every single project.

Target Market(s)

Design & Build Clients

Industry/Entity Type

Construction Company

Contact Information for Business Card

Address:
18 West Marlow Field Road, Unit 17, Dunmore Vale, ON, K7T 2M9
Office: 905-218-6937

Pollvarns Logo
Employee Job Description
Employee Cell Phone #
Employee Email
www.pollvarn.example

Colors

Designer to choose colors to be used in the design.

Requirements
Must have
• Quote Company Saying:
• "Professional. Quality. Service."
Nice to have
• New Crisp up to date look. simple & fresh ( Not to Busy)
Should not have
• NO BLUE PRINTS ON THE BUSINESS CARDS

```html
<!DOCTYPE html>
<html lang="en">
<head>
<meta charset="utf-8">
<title>Pollvarn Building Inc. — Business Card</title>
<link rel="stylesheet" href="https://fonts.googleapis.com/css2?family=Exo+2:wght@400;500;600&display=swap">
<style>
  :root {
    --teal: #0a8176;
    --ink: #2b2b2b;
    --paper: #ffffff;
    --backdrop: #e9e6e1;
    --line-soft: rgba(255,255,255,0.9);
  }
  * { margin: 0; padding: 0; box-sizing: border-box; }
  html, body {
    width: 1200px; height: 900px; overflow: hidden;
    background: var(--backdrop);
    font-family: "Exo 2", sans-serif;
  }
  .canvas { position: relative; width: 1200px; height: 900px; }
  .card {
    position: absolute; left: 250px; width: 700px; height: 400px;
    border-radius: 22px; overflow: hidden;
    box-shadow: 0 6px 18px rgba(0,0,0,0.12);
  }
  .card--front { top: 40px; background: var(--paper); }
  .card--back { top: 460px; background: var(--teal); }

  /* Brand block */
  .brand { display: flex; align-items: center; gap: 12px; }
  .brand__mark { width: 40px; height: 40px; background: var(--teal); flex: none; }
  .brand__name {
    font-weight: 600; font-size: 30px; letter-spacing: 1px;
    color: var(--teal); line-height: 1; white-space: nowrap;
  }
  .tagline {
    font-weight: 600; font-size: 17px; letter-spacing: 1px;
    color: var(--teal); white-space: nowrap;
  }

  .front-head { position: absolute; left: 48px; top: 40px; }
  .front-head .tagline { margin-top: 14px; }

  .person { position: absolute; left: 48px; top: 142px; }
  .person__name { font-weight: 600; font-size: 30px; letter-spacing: 1px; color: var(--teal); }
  .person__role { font-size: 13px; color: var(--ink); margin-top: 2px; }

  .rule { position: absolute; left: 48px; right: 48px; top: 228px; height: 2px; background: var(--teal); }
  .rule::before {
    content: ""; position: absolute; left: 0; top: -1.5px;
    width: 220px; height: 5px; background: var(--teal);
  }

  .contacts {
    position: absolute; left: 48px; right: 48px; top: 252px;
    font-size: 17px; color: var(--ink);
  }
  .contacts__row { display: flex; margin-bottom: 16px; }
  .contact { display: flex; white-space: nowrap; }
  .contact__label { font-weight: 600; color: var(--teal); width: 30px; }
  .contact--phone { width: 220px; }
  .contact--email { width: 400px; }

  /* Back */
  .back-foot {
    position: absolute; left: 40px; right: 40px; bottom: 40px;
    display: flex; align-items: flex-end;
  }
  .back-foot .brand__mark { background: var(--paper); width: 32px; height: 32px; }
  .back-foot .brand__name { color: var(--paper); font-size: 24px; }
  .back-foot .tagline { color: var(--paper); font-size: 14px; margin-top: 12px; }
  .back-rule {
    flex: 1; height: 2px; margin: 0 0 8px 24px;
    background: var(--line-soft);
  }
</style>
</head>
<body>
<main class="canvas">
  <section class="card card--front" aria-label="Business card front">
    <div class="front-head">
      <div class="brand">
        <span class="brand__mark"></span>
        <span class="brand__name">POLLVARN BUILDING INC.</span>
      </div>
      <p class="tagline">Professional . Quality . Service</p>
    </div>

    <div class="person">
      <h1 class="person__name">Marcus Hale</h1>
      <p class="person__role">CEO | Founder</p>
    </div>

    <div class="rule"></div>

    <div class="contacts">
      <div class="contacts__row">
        <div class="contact"><span class="contact__label">A :</span><span>18 West Marlow Field Road, Unit 17, Dunmore Vale, ON, K7T 2M9</span></div>
      </div>
      <div class="contacts__row">
        <div class="contact contact--phone"><span class="contact__label">P :</span><span>905-218-6937</span></div>
        <div class="contact"><span class="contact__label">C :</span><span>905-218-6937</span></div>
      </div>
      <div class="contacts__row">
        <div class="contact contact--email"><span class="contact__label">E :</span><span>hale@pollvarn.example</span></div>
        <div class="contact"><span class="contact__label">W :</span><span>www.pollvarn.example</span></div>
      </div>
    </div>
  </section>

  <section class="card card--back" aria-label="Business card back">
    <div class="back-foot">
      <div class="back-brand">
        <div class="brand">
          <span class="brand__mark"></span>
          <span class="brand__name">POLLVARN BUILDING INC.</span>
        </div>
        <p class="tagline">Professional . Quality . Service</p>
      </div>
      <div class="back-rule"></div>
    </div>
  </section>
</main>
</body>
</html>
```